Ridgely Forge business card for handing simple contact information and generating service awareness

Utilizing the attached logo(s), generate a professional, but approachable, card conveying a sense of capability and integrity. Please only use one logo of the four attached; the different colors are all acceptable, but preference will be given to a design integrating a teal/turquoise logo,

I do not know where to put in the contact information or details?

Target Market(s)

Agriculture, Farming, Timber, Forestry, Construction, Crane Service

Industry/Entity Type

Contact Information for Business Card

Name, Phone Number, email address

Colors

Designer to choose colors to be used in the design.

Requirements
Nice to have
• It would be great to have either a mountain or one of the attached cranes as a backdrop on the rear of the card. Simple watermarks and/or Debossing is also great

```html
<!DOCTYPE html>
<html lang="en">
<head>
<meta charset="utf-8">
<title>Ridgely Forge – Business Card</title>
<link rel="stylesheet" href="https://fonts.googleapis.com/css2?family=Lato:wght@400;700;900&display=swap">
<style>
  :root {
    --teal: #2a6f65;
    --teal-dark: #1f5a51;
    --white: #ffffff;
    --ink-grey: #5d5f61;
    --rule-grey: #a7a9ab;
    --backdrop: #e6e9e9;
  }
  * { margin: 0; padding: 0; box-sizing: border-box; }
  html, body {
    width: 1200px; height: 952px; overflow: hidden;
    background: var(--backdrop);
    font-family: "Lato", sans-serif;
  }
  .sheet {
    position: relative; width: 1200px; height: 952px;
    display: flex; align-items: center; justify-content: center; gap: 40px;
  }
  .card {
    position: relative; width: 540px; height: 308px;
    overflow: hidden;
    box-shadow: 0 6px 18px rgba(0,0,0,0.18);
  }

  /* Front */
  .card--front { background: var(--teal); display: flex; align-items: center; justify-content: center; }
  .wordmark {
    font-family: "Lato", sans-serif; font-weight: 900;
    text-transform: uppercase; letter-spacing: 1px; white-space: nowrap;
  }
  .card--front .wordmark { color: var(--white); font-size: 38px; }

  /* Back */
  .card--back { background: var(--white); }
  .card--back .wordmark {
    position: absolute; left: 28px; top: 110px; width: 210px;
    color: var(--teal); font-size: 26px; line-height: 1.1; text-align: center; white-space: normal;
  }
  .contact { position: absolute; left: 268px; top: 72px; }
  .contact__name { color: var(--teal); font-size: 19px; font-weight: 400; letter-spacing: 0.5px; text-transform: uppercase; }
  .contact__name strong { font-weight: 700; }
  .contact__title { color: var(--ink-grey); font-size: 13px; margin-top: 2px; }
  .contact__divider { width: 42px; height: 1px; background: var(--ink-grey); margin: 8px 0 10px; }
  .contact__list { list-style: none; }
  .contact__item {
    display: flex; align-items: flex-start; gap: 8px;
    color: var(--ink-grey); font-size: 11.5px; line-height: 1.35; margin-bottom: 6px;
  }
  .contact__icon {
    flex: 0 0 14px; width: 14px; height: 14px; border-radius: 3px;
    background: var(--teal); display: flex; align-items: center; justify-content: center; margin-top: 1px;
  }
  .contact__icon svg { width: 10px; height: 10px; }
  .edge-rules { position: absolute; left: 0; bottom: 0; width: 540px; height: 60px; }
</style>
</head>
<body>
<main class="sheet">

  <section class="card card--front" aria-label="Card front">
    <span class="wordmark">Ridgely Forge</span>
  </section>

  <section class="card card--back" aria-label="Card back">
    <span class="wordmark">Ridgely Forge</span>

    <div class="contact">
      <h1 class="contact__name">Holden R. <strong>Marsh</strong></h1>
      <p class="contact__title">Managing Director</p>
      <div class="contact__divider"></div>
      <ul class="contact__list">
        <li class="contact__item">
          <span class="contact__icon">
            <svg viewBox="0 0 10 10"><path d="M5 1a3 3 0 0 0-3 3c0 2.2 3 5 3 5s3-2.8 3-5a3 3 0 0 0-3-3z" fill="#fff"/><circle cx="5" cy="4" r="1.1" fill="#2a6f65"/></svg>
          </span>
          <span>2150 Cedar Ridge Road<br>Asheville, NC 28804</span>
        </li>
        <li class="contact__item">
          <span class="contact__icon">
            <svg viewBox="0 0 10 10"><path d="M2.2 1.2l1.6 1.7-.8 1.1c.6 1.2 1.5 2.1 2.7 2.7l1.1-.8 1.7 1.6-.9 1.3C4.8 8.6 1.4 5.2 1.2 2.1z" fill="#fff"/></svg>
          </span>
          <span>+00 987 654 32</span>
        </li>
        <li class="contact__item">
          <span class="contact__icon">
            <svg viewBox="0 0 10 10"><rect x="1" y="2.2" width="8" height="5.6" fill="none" stroke="#fff" stroke-width="1"/><path d="M1 2.4l4 3 4-3" fill="none" stroke="#fff" stroke-width="1"/></svg>
          </span>
          <span>hello@ridgelyforge.com</span>
        </li>
        <li class="contact__item">
          <span class="contact__icon">
            <svg viewBox="0 0 10 10"><path d="M2.5 1.5l5.5 3-2.3.7 1.6 2.6-1 .6-1.6-2.6-1.7 1.7z" fill="#fff"/></svg>
          </span>
          <span>www.ridgelyforge.com</span>
        </li>
      </ul>
    </div>

    <svg class="edge-rules" viewBox="0 0 540 60" aria-hidden="true">
      <line x1="0" y1="22" x2="192" y2="22" stroke="var(--rule-grey)" stroke-width="2.5"/>
      <polygon points="188,38 540,38 540,44 194,44" fill="var(--teal)"/>
    </svg>
  </section>

</main>
</body>
</html>
```